Cutaneous Learning Clinical Treatments workbook New Word Template Design Project

Cutaneous Learning needs the old "Harbourview Derma Procedures Handbook" updated and given a fresh new look, using the new Cutaneous Learning logo.

The old workbook will be supplied to act as a guideline, but we'd like a fresh new look.

Target Market(s)

The people using this workbook are Dermal therapists and Dermal nurses.

Font styles to use
Serif
Sans Serif

Requirements
Must have
• The new logo incorporated on each page - obviously on the cover it will be a major focus, but on other pages we'd like to see the logo represented in a smaller way somehow.

Each module is to follow the same formula - as per the old workbook.

A4 portrait - 210mm X 297mm (8-1/4 X 11-3/4 inches)

The end result will be printed, so there must be space on the LH side to allow for binding
Nice to have
• We'd like the colour scheme of the new design to work in/match with the colour scheme of the logo.

Request from my boss - the final products we will need back are:
(1) an editable "in design" file
(2) pdf document

```html
<!DOCTYPE html>
<html lang="en">
<head>
<meta charset="utf-8">
<title>Cutaneous Learning – Clinical Treatments Workbook spreads</title>
<link href="https://fonts.googleapis.com/css2?family=Oswald:wght@500;700&family=Montserrat:wght@500;700;800&family=Lato:wght@400;700&display=swap" rel="stylesheet">
<style>
:root{
  --navy:#141f5c;
  --gold:#a8892f;
  --gold-soft:#e3c257;
  --gold-row:#a88d3d;
  --ice:#d9eaf7;
  --ink:#1d1d24;
  --stage:#5f5e61;
  --teal:#2ba4c4;
  --orange:#f26a22;
  --green:#21b05a;
}
*{box-sizing:border-box;margin:0;padding:0}
html,body{width:1200px;height:1200px;overflow:hidden}
body{background:var(--stage);position:relative;font-family:"Lato",sans-serif;color:var(--ink)}

.page{position:absolute;overflow:hidden;box-shadow:0 2px 7px rgba(0,0,0,.4);
  background:linear-gradient(180deg,var(--ice) 0%,#fff 13%,#fff 82%,#d3e7f5 100%)}
.abs{position:absolute}
.footer-url{position:absolute;bottom:10px;left:0;right:0;text-align:center;font-size:5.6px;letter-spacing:.6px;color:#222;font-family:"Montserrat",sans-serif}
.mini-mark{position:absolute;right:12px;bottom:8px;display:flex;flex-direction:column;align-items:center;gap:1px}
.mini-mark i{display:block;width:9px;height:9px;background:var(--navy);border:1px solid var(--gold)}
.mini-mark b{font-size:2.6px;font-weight:700;color:var(--navy);white-space:nowrap}

/* pill heading with gold rules */
.pill-head{position:absolute;left:0;right:0;height:20px;display:flex;justify-content:center;align-items:center}
.pill-head::before,.pill-head::after{content:"";position:absolute;left:0;right:0;height:1.5px;background:var(--gold)}
.pill-head::before{top:7px}
.pill-head::after{top:11px;background:#c9b26a;height:.8px}
.pill{position:relative;z-index:1;background:var(--navy);color:#fff;font-family:"Oswald",sans-serif;font-weight:700;font-size:12px;letter-spacing:.3px;border-radius:11px;padding:1px 14px;line-height:17px;white-space:nowrap}
.pill.sm{font-size:7.5px;line-height:11px;padding:0 10px;border-radius:7px}

.body-text{position:absolute;font-size:4.3px;line-height:1.35;color:#222}
.body-text p{margin-bottom:3px}

.photo{position:absolute}

/* cover */
.cover-mark{position:absolute;left:0;right:0;top:66px;display:flex;flex-direction:column;align-items:center;gap:8px}
.cover-mark i{width:34px;height:34px;background:var(--navy);border:2px solid var(--gold)}
.cover-mark b{font-family:"Lato",sans-serif;font-weight:700;font-size:11px;letter-spacing:1.5px;color:var(--navy);text-transform:uppercase}
.cover-title{position:absolute;left:26px;font-family:"Oswald",sans-serif;font-weight:700;color:var(--navy);line-height:1}
.cover-title .gold{color:var(--gold-soft)}
.cover-band{position:absolute;left:0;right:0;top:248px;height:26px;background:var(--navy);color:var(--gold-soft);font-family:"Oswald",sans-serif;font-weight:500;font-size:19px;line-height:26px;padding-left:40px;letter-spacing:.2px}
.staff-line{position:absolute;left:32px;top:292px;font-family:"Montserrat",sans-serif;font-size:7px;display:flex;align-items:flex-end;gap:4px}
.staff-line span{display:block;width:164px;border-bottom:1px solid #333;height:8px}

/* contents */
.content-word{position:absolute;left:8px;top:365px;transform-origin:0 0;transform:rotate(-90deg);font-family:"Montserrat",sans-serif;font-weight:800;font-size:66px;letter-spacing:2px;color:var(--navy);line-height:1}
.gold-bar{position:absolute;top:0;width:17px;height:84px;background:var(--gold)}
.toc-h{position:absolute;left:73px;font-family:"Montserrat",sans-serif;font-weight:500;font-size:10px;color:var(--ink)}
.toc-h.intro{display:flex;width:196px;align-items:baseline}
.toc-h.intro .dots{flex:1;border-bottom:1px dotted #333;margin:0 2px}
.toc-rule{position:absolute;left:73px;width:198px;height:1px;background:var(--gold)}
.toc{position:absolute;left:73px;width:196px;list-style:none}
.toc li{display:flex;align-items:baseline;font-size:4.9px;height:13.7px;font-family:"Montserrat",sans-serif;color:#222;text-transform:uppercase}
.toc li .dots{flex:1;border-bottom:.6px dotted #444;margin:0 1px}

/* summary table */
.summary-table{position:absolute;left:12px;top:47px;width:251px;border-collapse:collapse;font-size:5.4px;font-family:"Montserrat",sans-serif;text-transform:uppercase;color:#222;border:.6px solid #8aa0c8}
.summary-table td{height:19.9px;vertical-align:middle;padding:0 6px;line-height:1.15}
.summary-table td.num{width:46px;white-space:nowrap}
.summary-table td.name{width:128px;border-right:.6px solid #8aa0c8}
.summary-table tr:nth-child(odd) td{background:var(--gold-soft)}
.summary-table tr:nth-child(odd) td.date{background:var(--gold-soft)}
.summary-table tr:nth-child(even) td{background:#fff}
.summary-table td.date{width:77px}

/* sign-off check table */
.check-table{position:absolute;left:9px;top:58px;width:259px;border-collapse:collapse;font-size:4.6px;color:#222}
.check-table td,.check-table th{border:.6px solid #555;padding:1px 3px;height:14.5px;vertical-align:middle;line-height:1.2;text-align:left}
.check-table th{font-weight:400;text-align:center;height:16px;background:#fff}
.check-table td.box{width:30px}
.check-table tr.goldrow td{background:var(--gold-row);color:#fff}
.sig-row{position:absolute;left:12px;width:254px;display:flex;font-size:4.6px;align-items:flex-end;gap:3px}
.sig-row span.line{flex:1;border-bottom:.6px solid #555;height:5px}

/* photography sign-off */
.photo-table{position:absolute;left:18px;top:62px;width:238px;border-collapse:collapse;font-size:4.5px;color:#333}
.photo-table th{color:#fff;font-weight:400;height:18px;font-size:4.2px;border:.8px solid #fff}
.photo-table td{border:.6px solid #9aa8c4;height:15.8px;text-align:center;line-height:1.1;background:rgba(255,255,255,.7)}
.photo-table td:first-child{width:50px}
.qa{position:absolute;left:18px;width:190px;display:flex;align-items:center;font-size:5px;color:#333}
.qa .q{flex:1}
.qa .y,.qa .n{width:21px;height:7px;font-size:4.2px;text-align:center;line-height:7px;color:#fff;margin-left:1px}
.qa .y{background:var(--navy)}
.qa .n{background:var(--gold)}

.steps{position:absolute;font-size:4.5px;line-height:1.35;color:#222;list-style:none}
.steps li{margin-bottom:4px}
</style>
</head>
<body>

<!-- COVER -->
<section class="page" style="left:20px;top:17px;width:280px;height:393px">
  <div class="cover-mark"><i></i><b>Cutaneous Learning</b></div>
  <div class="cover-title" style="top:166px;font-size:25px">CLINICAL <span class="gold">TREATMENTS</span></div>
  <div class="cover-title" style="top:192px;font-size:46px;letter-spacing:.5px">WORKBOOK</div>
  <div class="cover-band">CUTANEOUS LEARNING</div>
  <div class="staff-line">STAFF NAME :<span></span></div>
  <div class="footer-url">www.cutaneouslearning.edu</div>
</section>

<!-- CONTENTS 1 -->
<section class="page" style="left:308px;top:15px;width:278px;height:393px">
  <div class="gold-bar" style="left:73px"></div>
  <div class="content-word">CONTENT</div>
  <div class="toc-h intro" style="top:91px">INTRODUCTION<span class="dots"></span>3</div>
  <div class="toc-h" style="top:113px">WORKBOOK SUMMARY</div>
  <div class="toc-rule" style="top:127px"></div>
  <ol class="toc" style="top:134px">
    <li>Module 1 : Documentation for treatments<span class="dots"></span>4</li>
    <li>Module 2: Medical photography<span class="dots"></span>5</li>
    <li>Module 3: Infection prevention &amp; control<span class="dots"></span>18</li>
    <li>Module 4: Sterilisation<span class="dots"></span>26</li>
    <li>Module 5: Workspace maintenance<span class="dots"></span>33</li>
    <li>Module 6: Pathology collection<span class="dots"></span>40</li>
    <li>Module 7: Drugs &amp; poisons regulation<span class="dots"></span>47</li>
    <li>Module 8: Pre-op calls to patients<span class="dots"></span>48</li>
    <li>Module 8: Pre-op calls to patients<span class="dots"></span>49</li>
    <li>Module 10: Following up your patient post treatment<span class="dots"></span>50</li>
    <li>Module 11: Chemical peels<span class="dots"></span>57</li>
    <li>Module 12: Extractions (with Hyfrotip)<span class="dots"></span>58</li>
    <li>Module 13: L.E.D treatment<span class="dots"></span>49</li>
    <li>Module 14: Hair removal<span class="dots"></span>49</li>
    <li>Module 15: Broad band light treatment (BBL)<span class="dots"></span>49</li>
    <li>Module 16: Fractionated laser (Fractilux)<span class="dots"></span>49</li>
  </ol>
  <div class="footer-url">www.cutaneouslearning.edu</div>
  <div class="mini-mark"><i></i><b>Cutaneous Learning</b></div>
</section>

<!-- CONTENTS 2 -->
<section class="page" style="left:592px;top:15px;width:280px;height:393px">
  <div class="gold-bar" style="left:73px"></div>
  <div class="content-word">CONTENT</div>
  <div class="toc-h" style="top:117px">WORKBOOK SUMMARY</div>
  <div class="toc-rule" style="top:132px"></div>
  <ol class="toc" style="top:144px">
    <li>Module 17: Biophotonic treatment (Lumiresca)<span class="dots"></span>49</li>
    <li>Module 18: Mela peels<span class="dots"></span>49</li>
    <li>Module 19: Pulsed dye laser (VascuBeam)<span class="dots"></span>49</li>
    <li>Module 20: Pico-second laser (pico for pigment)<span class="dots"></span>49</li>
    <li>Module 21: Pico-second laser (pico tattoo removal)<span class="dots"></span>49</li>
    <li>Module 22: RF needling<span class="dots"></span>49</li>
    <li>Module 23: Micro pen<span class="dots"></span>49</li>
    <li>Module 24: Skin tightening (Thermaform)<span class="dots"></span>49</li>
    <li>Module 25: Skin tightening (RF tightening)<span class="dots"></span>49</li>
    <li>Module 26: ChillContour<span class="dots"></span>49</li>
    <li>Module 27: Skin tag removal<span class="dots"></span>49</li>
    <li>Module 28: DryWave<span class="dots"></span>49</li>
    <li>Module 29: PRP<span class="dots"></span>49</li>
    <li>Module 30: Injectables<span class="dots"></span>49</li>
  </ol>
  <div class="footer-url">www.cutaneouslearning.edu</div>
  <div class="mini-mark"><i></i><b>Cutaneous Learning</b></div>
</section>

<!-- INTRODUCTION -->
<section class="page" style="left:882px;top:15px;width:281px;height:394px">
  <div class="pill-head" style="top:10px"><span class="pill">INTRODUCTION</span></div>
  <div class="body-text" style="left:18px;top:36px;width:250px">
    <p>Welcome to our clinical team! We hope that you enjoy your time as a member of our dermatology team. To assist with your induction, please complete all sections of this workbook and bring it to your progress meetings with your manager.</p>
    <p>Links to the theoretical components and exams can be found on our intranet, where we keep all of our reading material and videos.</p>
    <p>All of your practical sheets in this workbook must be signed by an experienced member of our team.</p>
  </div>
  <div class="abs" style="left:0;top:92px;width:130px;height:11px;background:linear-gradient(90deg,var(--gold),#e0c766);clip-path:polygon(0 0,100% 0,94% 100%,0 100%)"></div>
  <div class="photo" role="img" aria-label="Photo of a clinician with stethoscope and floating medical icons" style="left:0;top:103px;width:281px;height:124px;background:linear-gradient(120deg,#cfe2f0 0%,#9dbfd8 45%,#e8f1f8 70%,#6d93b5 100%)"></div>
  <div class="abs" style="left:14px;top:187px;width:125px;height:23px;background:var(--navy);color:#fff;font-size:3.8px;line-height:1.3;padding:3px 5px">NOTE : THIS WORKBOOK MUST REMAIN IN A SECURE PLACE AT WORK, AS IT CONTAINS PATIENT INFORMATION AND MUST NOT BE TAKEN OUTSIDE THE PRACTICE.</div>
  <div class="abs" style="left:150px;top:224px;width:131px;height:10px;background:linear-gradient(90deg,#e0c766,var(--gold));clip-path:polygon(6% 0,100% 0,100% 100%,0 100%)"></div>
  <div class="body-text" style="left:10px;top:244px;width:262px">
    <p>Please also fill out the sign off sheet for each module to ensure that you have completed all components of the module and present to your manager for approval to begin treating patients.</p>
    <p>Progress meetings are highly recommended to make sure you are on the right track before you have completed too many sections and to make sure you are not needing to repeat any work!</p>
    <p>You are expected to have completed modules 1 - 17 within 4 weeks of starting and modules 17 - 27 as arranged with your manager. Modules 28-30 are for nurses only, as arranged with your manager also. Please get busy finding opportunities to complete these sections - enjoy!</p>
  </div>
  <div class="pill-head" style="top:310px"><span class="pill sm">HOW TO FINISH THIS WORKBOOK</span></div>
  <ol class="steps" style="left:9px;top:333px;width:125px">
    <li>1. Read online theory and videos for each module</li>
    <li>2. Complete online exam for each module</li>
    <li>3. Complete observations on your sign off sheet</li>
  </ol>
  <ol class="steps" style="left:145px;top:335px;width:128px">
    <li>4. Complete practical sheets in this workbook</li>
    <li>5. Present completed sign off sheet to your manager for approval to begin each task</li>
  </ol>
  <div class="footer-url">www.cutaneouslearning.edu</div>
  <div class="mini-mark"><i></i><b>Cutaneous Learning</b></div>
</section>

<!-- WORKBOOK SUMMARY -->
<section class="page" style="left:17px;top:425px;width:275px;height:386px">
  <div class="pill-head" style="top:11px;justify-content:flex-start;padding-left:62px"><span class="pill">WORKBOOK SUMMARY</span></div>
  <div class="abs" style="left:196px;top:35px;font-family:'Oswald',sans-serif;font-size:6.5px;color:var(--navy)">DATE OF COMPLETION</div>
  <table class="summary-table">
    <tr><td class="num">MODULE 1:</td><td class="name">DOCUMENTATION FOR TREATMENTS</td><td class="date"></td></tr>
    <tr><td class="num">MODULE 2:</td><td class="name">MEDICAL PHOTOGRAPHY</td><td class="date"></td></tr>
    <tr><td class="num">MODULE 3:</td><td class="name">INFECTION PREVENTION &amp; CONTROL</td><td class="date"></td></tr>
    <tr><td class="num">MODULE 4:</td><td class="name">STERILISATION</td><td class="date"></td></tr>
    <tr><td class="num">MODULE 5:</td><td class="name">WORKSPACE MAINTENANCE</td><td class="date"></td></tr>
    <tr><td class="num">MODULE 6:</td><td class="name">PATHOLOGY COLLECTION</td><td class="date"></td></tr>
    <tr><td class="num">MODULE 7:</td><td class="name">DRUGS &amp; POISONS REGULATION</td><td class="date"></td></tr>
    <tr><td class="num">MODULE 8:</td><td class="name">PRE-OP CALLS TO PATIENTS</td><td class="date"></td></tr>
    <tr><td class="num">MODULE 9:</td><td class="name">ADMINISTERING NUMBING CREAM</td><td class="date"></td></tr>
    <tr><td class="num">MODULE 10:</td><td class="name">FOLLOWING UP YOUR PATIENT POST TREATMENT</td><td class="date"></td></tr>
    <tr><td class="num">MODULE 11:</td><td class="name">CHEMICAL PEELS</td><td class="date"></td></tr>
    <tr><td class="num">MODULE 12:</td><td class="name">EXTRACTIONS (WITH HYFROTIP)</td><td class="date"></td></tr>
    <tr><td class="num">MODULE 13:</td><td class="name">L.E.D TREATMENT</td><td class="date"></td></tr>
    <tr><td class="num">MODULE 14:</td><td class="name">HAIR REMOVAL</td><td class="date"></td></tr>
    <tr><td class="num">MODULE 15:</td><td class="name">BROAD BAND LIGHT TREATMENT (BBL)</td><td class="date"></td></tr>
    <tr><td class="num">MODULE 16:</td><td class="name">FRACTIONATED LASER (FRACTILUX)</td><td class="date"></td></tr>
  </table>
  <div class="footer-url" style="bottom:8px">www.cutaneouslearning.edu</div>
  <div class="mini-mark"><i></i><b>Cutaneous Learning</b></div>
</section>

<!-- DOCUMENTATION FOR TREATMENTS -->
<section class="page" style="left:303px;top:420px;width:277px;height:388px">
  <div class="pill-head" style="top:10px"><span class="pill">DOCUMENTATION FOR TREATMENTS</span></div>
  <div class="photo" role="img" aria-label="Photo of a stethoscope resting on medical notes" style="left:0;top:30px;width:277px;height:100px;background:linear-gradient(110deg,#dfe6e4 0%,#b9cfc9 35%,#d8c7ad 65%,#efe3d2 100%)"></div>
  <div class="abs" style="left:146px;top:95px;width:127px;height:23px;background:var(--navy);color:#fff;font-size:4.4px;line-height:1.3;padding:3px 4px">Strong medical note taking is imperative in any medical setting. If it's not written down, it didn't happen.</div>
  <div class="body-text" style="left:19px;top:139px;width:244px">
    <p>The theoretical components provide guidance on what components make a good medical note for when you are treating patients. Please refer to the online training module to complete your theory.</p>
    <p>The practical component is a review of the first 20 medical notes for treatments made by the clinician seeking to be signed off. This review may be done by an experienced clinician or manager, and is to be done incrementally to allow for feedback along the way.</p>
    <p>For each medical note reviewed, please have the clinician or manager fill out the practical sheet and sign it for you.</p>
    <p>Fill out the summary sign off sheet to track your progress and present to your manager once completed.</p>
  </div>
  <div class="photo" role="img" aria-label="Illustration of a hand holding a tablet with glowing molecular graphics" style="left:0;top:202px;width:277px;height:104px;background:linear-gradient(180deg,rgba(255,255,255,0) 0%,#cfe3f3 30%,#a9c9e2 70%,#e9f2f9 100%)"></div>
  <div class="pill-head" style="top:305px"><span class="pill sm">HOW TO FINISH THIS MODULE</span></div>
  <ol class="steps" style="left:9px;top:328px;width:128px">
    <li>1. Read online theory (refer to "medical staff -&gt; documentation")</li>
    <li>2. Watch online video (refer to "medical staff -&gt; documentation")</li>
  </ol>
  <ol class="steps" style="left:144px;top:328px;width:128px">
    <li>3. Complete online exam (refer to "modules &amp; exams -&gt; documentation")</li>
    <li>4. Complete practical sheets in this workbook</li>
  </ol>
  <div class="footer-url" style="bottom:8px">www.cutaneouslearning.edu</div>
  <div class="mini-mark"><i></i><b>Cutaneous Learning</b></div>
</section>

<!-- DOCUMENTATION SIGN-OFF -->
<section class="page" style="left:591px;top:417px;width:276px;height:387px">
  <div class="pill-head" style="top:10px"><span class="pill" style="font-size:9.5px">DOCUMENTATION FOR TREATMENTS SIGN-OFF SHEET</span></div>
  <div class="abs" style="left:9px;top:42px;width:260px;display:flex;font-size:5.2px;align-items:flex-end;gap:2px">
    Patient Name :<span style="flex:1;border-bottom:.7px solid #333;height:5px"></span>
    Treatment Type :<span style="flex:1;border-bottom:.7px solid #333;height:5px"></span>
    Date :<span style="width:30px;border-bottom:.7px solid #333;height:5px"></span>
  </div>
  <table class="check-table">
    <tr><th style="border-right:none"></th><th class="box">YES</th><th class="box">NO</th><th class="box">NA</th></tr>
    <tr class="goldrow"><td>A note has been made in the medical desktop for this treatment</td><td class="box"></td><td class="box"></td><td class="box"></td></tr>
    <tr><td>Note made as a new medical note, with the correct practitioner name, and saved correctly to the patient file with concise description line</td><td></td><td></td><td></td></tr>
    <tr><td>Correct consent forms given to patient prior to treatment</td><td></td><td></td><td></td></tr>
    <tr class="goldrow"><td>Patient concerns recorded in medical desktop</td><td></td><td></td><td></td></tr>
    <tr><td>Consent forms discussed prior to treatment, and discussion noted in medical desktop</td><td></td><td></td><td></td></tr>
    <tr class="goldrow"><td>Consent forms fully signed and given to admin for scanning before treating next patient</td><td></td><td></td><td></td></tr>
    <tr><td>Treatment discussed with patient and noted in medical desktop</td><td></td><td></td><td></td></tr>
    <tr class="goldrow"><td>Aftercare discussed and patient understanding noted in medical desktop</td><td></td><td></td><td></td></tr>
    <tr><td>Medications given recorded (eg numbing cream) in medical desktop</td><td></td><td></td><td></td></tr>
    <tr class="goldrow"><td>Settings used recorded in medical desktop</td><td></td><td></td><td></td></tr>
    <tr><td>Treatment Proforma fully filled, signed and given to admin for scanning before treating next patient</td><td></td><td></td><td></td></tr>
    <tr class="goldrow"><td>Aftercare discussed and patient understanding noted in medical desktop</td><td></td><td></td><td></td></tr>
    <tr><td>Aftercare sheet given and noted in medical desktop</td><td></td><td></td><td></td></tr>
  </table>
  <div class="sig-row" style="top:304px">Observing Clinician Name :<span class="line"></span>Signature :<span class="line" style="flex:.6"></span></div>
  <div class="sig-row" style="top:318px">Staff Member in Training :<span class="line"></span>Signature :<span class="line" style="flex:.6"></span></div>
  <div class="footer-url" style="bottom:8px">www.cutaneouslearning.edu</div>
  <div class="mini-mark"><i></i><b>Cutaneous Learning</b></div>
</section>

<!-- MEDICAL PHOTOGRAPHY -->
<section class="page" style="left:887px;top:417px;width:276px;height:387px">
  <div class="pill-head" style="top:8px"><span class="pill">02 MEDICAL PHOTOGRAPHY</span></div>
  <div class="photo" role="img" aria-label="Photo of a person setting up a camera on a tripod in a bright studio" style="left:0;top:37px;width:123px;height:86px;background:linear-gradient(135deg,#eef2f5 0%,#d9c4c4 45%,#4a4f5a 60%,#e7ebef 100%)"></div>
  <div class="abs" style="left:123px;top:37px;width:153px;height:86px;background:var(--navy);clip-path:polygon(8% 0,100% 0,100% 100%,0 100%);color:#fff;font-family:'Oswald',sans-serif;font-weight:500;font-size:10.5px;line-height:1.28;padding:12px 10px 0 23px">Taking good medical photographs is an artform that requires great attention to detail.</div>
  <div class="body-text" style="left:9px;top:132px;width:258px">
    <p>The theoretical components provide guidance on how to take good photographs for different areas of the body with a special focus on five point photographs for the face. Please refer to the online training module to complete your theory.</p>
    <p>The practical component is a review of the first 5 sets of medical photographs you make by the staff member seeking to be signed off. This review may be done by an experienced staff member or manager, and is to be done incrementally to allow for feedback along the way. For each set of medical photographs reviewed, please have the nurse or manager fill out the practical sheet and sign it for you. Fill out the summary sign off sheet to track your progress and present to your manager once completed.</p>
  </div>
  <div class="abs" style="left:12px;top:200px;font-family:'Oswald',sans-serif;font-weight:700;font-size:13px;line-height:1.05;color:var(--gold)">HOW TO FINISH<br>THIS MODULE</div>
  <div class="photo" role="img" aria-label="Photo of a gloved hand holding dental instruments over a tray" style="left:135px;top:200px;width:141px;height:100px;background:linear-gradient(135deg,#f1f5f8 0%,#9ec3df 40%,#3e6fa3 70%,#c7d8e6 100%);clip-path:polygon(6% 0,100% 0,100% 100%,0 100%)"></div>
  <ol class="steps" style="left:12px;top:236px;width:118px">
    <li>1. Read online theory (refer to "medical staff -&gt; photography")</li>
    <li>2. Watch online video (refer to "medical staff -&gt; photography")</li>
    <li>3. Complete online exam (refer to "modules &amp; exams -&gt;photography")</li>
    <li>4. Complete practical sheets in this workbook</li>
  </ol>
  <div class="footer-url" style="bottom:8px">www.cutaneouslearning.edu</div>
  <div class="mini-mark"><i></i><b>Cutaneous Learning</b></div>
</section>

<!-- MEDICAL PHOTOGRAPHY SIGN OFF -->
<section class="page" style="left:492px;top:818px;width:264px;height:369px">
  <div class="pill-head" style="top:8px"><span class="pill" style="font-size:10.5px">MEDICAL PHOTOGRAPHY SIGN OFF SHEET</span></div>
  <div class="abs" style="left:18px;top:40px;width:210px;display:flex;align-items:flex-end;gap:3px;font-family:'Montserrat',sans-serif;font-size:6.8px">STAFF NAME:<span style="flex:1;border-bottom:.7px solid #555;height:6px"></span></div>
  <table class="photo-table">
    <tr><th style="background:var(--teal);width:50px">TYPE</th><th style="background:var(--orange);width:44px">DATE</th><th style="background:var(--green);width:42px">PATIENT NAME</th><th style="background:var(--navy)">EXPERIENCED STAFF MEMBER NAME</th></tr>
    <tr><td>Observation</td><td></td><td></td><td></td></tr>
    <tr><td>Observation</td><td></td><td></td><td></td></tr>
    <tr><td>Observation</td><td></td><td></td><td></td></tr>
    <tr><td>Observation</td><td></td><td></td><td></td></tr>
    <tr><td>Observation</td><td></td><td></td><td></td></tr>
    <tr><td>Supervised photo taking</td><td></td><td></td><td></td></tr>
    <tr><td>Supervised photo taking</td><td></td><td></td><td></td></tr>
    <tr><td>Supervised photo taking</td><td></td><td></td><td></td></tr>
    <tr><td>Supervised photo taking</td><td></td><td></td><td></td></tr>
    <tr><td>Supervised photo taking</td><td></td><td></td><td></td></tr>
  </table>
  <div class="qa" style="top:262px"><span class="q">Confident in taking medical photographs?</span><span class="y">Yes</span><span class="n">No</span></div>
  <div class="qa" style="top:275px"><span class="q">Confident in renaming photographs?</span><span class="y">Yes</span><span class="n">No</span></div>
  <div class="qa" style="top:288px"><span class="q">Module Completed and approved by manager?</span><span class="y">Yes</span><span class="n">No</span></div>
  <div class="sig-row" style="top:305px;left:18px;width:238px">Manager's Name :<span class="line"></span>Signature :<span class="line" style="flex:.7"></span></div>
  <div class="sig-row" style="top:318px;left:18px;width:238px">Staff Name :<span class="line"></span>Signature :<span class="line" style="flex:.7"></span></div>
  <div class="abs" style="left:18px;top:331px;font-size:4.8px">Date :&nbsp;&nbsp;&nbsp;&nbsp;&nbsp;/&nbsp;&nbsp;&nbsp;&nbsp;&nbsp;&nbsp;/</div>
  <div class="footer-url" style="bottom:7px">www.cutaneouslearning.edu</div>
  <div class="mini-mark"><i></i><b>Cutaneous Learning</b></div>
</section>

</body>
</html>
```